Quillby Foods logo

I am a catering and food business that requires a logo for my website and all related business branding. I also need a label for my hot sauce. You can find my information on Pallaview and there is a picture of the logo I currently use and also a bottle of my hot sauce.
I am based in the Adelaide Hills in South Australia. I would like to use black and gold or Purple and gold my colour scheme and really like the hornet cartoon that I currently use. Something more refined and original would be great...

```html
<!DOCTYPE html>
<html lang="en">
<head>
<meta charset="utf-8">
<title>Quillby Sauce – Bottle Label</title>
<link rel="stylesheet" href="https://fonts.googleapis.com/css2?family=Source+Sans+3:wght@400;700;900&display=swap">
<style>
  :root {
    --page: #ffffff;
    --label-paper: #ffffff;
    --band-navy: #011722;
    --gold: #ffd400;
    --gold-deep: #f0a800;
    --ink-light: #ffffff;
    --shadow: rgba(0, 0, 0, 0.35);
  }
  * { margin: 0; padding: 0; box-sizing: border-box; }
  html, body {
    width: 900px;
    height: 1200px;
    overflow: hidden;
    background: var(--page);
  }
  .canvas {
    position: relative;
    width: 900px;
    height: 1200px;
  }
  .label {
    position: absolute;
    left: 200px;
    top: 112px;
    width: 500px;
    height: 968px;
    background: var(--label-paper);
    box-shadow: 3px 4px 6px var(--shadow);
    overflow: hidden;
  }
  .label__band {
    position: absolute;
    left: 91px;
    top: 0;
    width: 323px;
    height: 100%;
    background: var(--band-navy);
  }
  .label__disc {
    position: absolute;
    left: 32px;
    top: 5px;
    width: 436px;
    height: 436px;
  }
  .mascot {
    position: absolute;
    left: 95px;
    top: 20px;
    width: 290px;
    height: 340px;
    border-radius: 46% 46% 42% 42%;
    background: radial-gradient(ellipse at 50% 40%, var(--gold) 0%, var(--gold-deep) 38%, #2a2a2a 70%, var(--band-navy) 100%);
    opacity: 0.9;
  }
  .product-name {
    position: absolute;
    left: 0;
    top: 345px;
    width: 100%;
    text-align: center;
    font-family: "Source Sans 3", sans-serif;
    font-weight: 900;
    font-size: 92px;
    line-height: 0.86;
    color: var(--gold);
    letter-spacing: 1px;
  }
  .label__copy {
    position: absolute;
    left: 91px;
    width: 323px;
    text-align: center;
    font-family: "Source Sans 3", sans-serif;
    font-weight: 400;
    font-size: 16.5px;
    line-height: 23px;
    color: var(--ink-light);
  }
  .descriptor { top: 542px; }
  .ingredients { top: 610px; padding: 0 14px; }
  .best-before { top: 741px; }
  .producer { top: 804px; }
  .volume {
    top: 913px;
    font-size: 22px;
  }
</style>
</head>
<body>
  <main class="canvas">
    <article class="label">
      <div class="label__band"></div>
      <svg class="label__disc" viewBox="0 0 436 436" aria-hidden="true">
        <circle cx="218" cy="218" r="218" fill="var(--band-navy)"/>
      </svg>
      <div class="mascot" role="img" aria-label="Cartoon hornet chef mascot in a white chef's hat holding a spatula"></div>
      <h1 class="product-name">Quillby<br>Sauce</h1>

      <p class="label__copy descriptor">HOT SAUCE, MARINADE, CONDIMENT<br>AND EXTREME FLAVOUR BRINGER</p>
      <p class="label__copy ingredients">INGREDIENETS: CAPSICUM, WATER, VINEGAR, sugar, GARLIC, lemon juice, olive oil, chilli, SPICES, CORNSTARCH, ALMOND, SALT.</p>
      <p class="label__copy best-before">Best Before: feb 2013</p>
      <p class="label__copy producer">Product of Australia<br>Quillby foods<br>48 larkspur lane brindle vale sa 5999</p>
      <p class="label__copy volume">250 ML</p>
    </article>
  </main>
</body>
</html>
```